New Business Card Design Project

Details for my new Business Card Design Project will be added soon. Like a nice simple design

Target Market(s)

Home improvement

Industry/Entity Type

Home Improvement

Contact Information for Business Card

Roofing siding gutters additions garages decks

Requirements
Must have
• Phone 5097362418
• Email korvandpm@mailnest.net

```html
<!DOCTYPE html>
<html lang="en">
<head>
<meta charset="utf-8">
<title>Dana Mercer – Business Card</title>
<link href="https://fonts.googleapis.com/css2?family=Oswald:wght@600&family=Lato:wght@400&family=Russo+One&display=swap" rel="stylesheet">
<style>
  :root {
    --backdrop: #2b2b2b;
    --card: #f2f2f3;
    --red: #e31e24;
    --blue: #0f7fc1;
    --ink: #1a1a1a;
    --tag-blue: #c3d6ea;
    --tag-peach: #f2c4b3;
  }
  * { margin: 0; padding: 0; box-sizing: border-box; }
  html, body {
    width: 1200px;
    height: 900px;
    overflow: hidden;
    background: var(--backdrop);
  }
  .canvas {
    position: relative;
    width: 1200px;
    height: 900px;
  }
  .card {
    position: absolute;
    left: 100px;
    top: 164px;
    width: 1000px;
    height: 572px;
    background: var(--card);
    overflow: hidden;
  }
  .accent-bar {
    position: absolute;
    left: 585px;
    top: 78px;
    right: 0;
    height: 50px;
    background: var(--red);
    border-radius: 8px 0 0 8px;
  }
  .name {
    position: absolute;
    left: 118px;
    top: 88px;
    font-family: "Oswald", sans-serif;
    font-weight: 600;
    font-size: 60px;
    line-height: 1;
    letter-spacing: -0.5px;
    text-transform: uppercase;
  }
  .name .first { color: var(--red); }
  .name .last { color: var(--blue); }
  .contacts {
    position: absolute;
    left: 118px;
    top: 172px;
    list-style: none;
    font-family: "Lato", sans-serif;
    font-size: 25px;
    color: var(--ink);
  }
  .contacts li {
    display: flex;
    align-items: center;
    gap: 8px;
    height: 34px;
  }
  .contacts .icon {
    width: 24px;
    height: 24px;
    flex: none;
  }
  .services {
    position: absolute;
    right: 18px;
    bottom: 20px;
    font-family: "Russo One", sans-serif;
    font-size: 84px;
    line-height: 0.8;
    text-align: right;
    color: var(--tag-blue);
    letter-spacing: -1px;
  }
  .services .line { display: block; }
  .services .peach { color: var(--tag-peach); }
</style>
</head>
<body>
<div class="canvas">
  <article class="card">
    <div class="accent-bar"></div>

    <h1 class="name"><span class="first">Dana</span><span class="last">Mercer</span></h1>

    <ul class="contacts">
      <li>
        <svg class="icon" viewBox="0 0 24 24" aria-hidden="true">
          <rect width="24" height="24" rx="5" fill="#e31e24"/>
          <rect x="7" y="4" width="10" height="16" rx="2" fill="none" stroke="#fff" stroke-width="1.8"/>
          <line x1="10" y1="17" x2="14" y2="17" stroke="#fff" stroke-width="1.6"/>
        </svg>
        <span>5097362418</span>
      </li>
      <li>
        <svg class="icon" viewBox="0 0 24 24" aria-hidden="true">
          <rect width="24" height="24" rx="5" fill="#e31e24"/>
          <text x="12" y="17.5" text-anchor="middle" font-family="Lato, sans-serif" font-size="16" fill="#fff">@</text>
        </svg>
        <span>korvandpm@mailnest.net</span>
      </li>
    </ul>

    <p class="services">
      <span class="line">roofing, <span class="peach">siding</span></span>
      <span class="line">gutter, <span class="peach">additions</span></span>
      <span class="line">handyman services</span>
    </p>
  </article>
</div>
</body>
</html>
```